New Agency Branding - Logo & Business Card

Project Description

ZUM is a creative agency that crafts memorable product experiences through meaningful design. By channeling the needs of the business and its customers, we are able to construct solutions that are elegant yet effective, powerful yet playful, and familiar yet stimulating.

In addition to our focus towards creating excellent products, we firmly believe that building a strong company culture is paramount. Our values revolve around building an environment that is passionate, supportive, collaborative, curious, humorous, and healthy. The ZUM team is relatively small, and we intend on keep this family tight-knit. We take great care in deciding who we work with and what we work on.

What we’re looking for is a designer who is willing to take on the challenge of helping us visually define and express the ZUM brand. We must comfortably occupy the consumer, commercial, and enterprise sectors. This means looking professional without sacrificing charm. We’re passionate about design and we care about people.

Deliverables

Logo

The first exercise would be to create the ZUM LOGO by referencing the concept that is attached (filename: ZUM Concept Logo). We like the idea of utilizing negative space, but are open to other suggestions. In terms of color, we’ve been flirting with the idea of purple as the primary color, but are again open to other explorations. The logo should be bold, professional, playful, and versatile (it should look just as crisp blown up on a website as it would on a contract).

Accepted Format(s): Adobe Illustrator (.ai) 

Business Card

The second exercise would be to design a business card utilizing the logo. The shape can be standard or square (single our double-sided), and must include the following:

• ZUM LOGO
• Tagline: "human experiences, designed"
• First and Last Name
• Job Role
• Contact Information (email address and phone number)
• Website URL

In terms of typography, we’d like to see considered pairings that compliment the logo, are legible, and can cohesively translate to other mediums (i.e. the ZUM website).

Accepted Format(s): Adobe Photoshop (.psd) OR Adobe Illustrator (.ai)

Style Guide

Finally, we’d like to have the brand defined and presented in a style guide. This would include the full color palette (primary color, secondary color, etc.) and font usage. In addition, we’d like to see rationale clearly communicated for the decisions made.

Visual References

Companies that inspire us:

morrow+venn
http://www.morrowvenn.example/story/morrow-venn/

BRISK
http://www.briskstudio.example

NestHop
https://www.nesthop.example

Fundlark
https://www.fundlark.example

Target Market(s)

Startups, Small to Mid Sized Businesses, Consultant Businesses

Industry/Entity Type

Design Agency

Contact Information for Business Card

FRONT: ZUM LOGO on White background

BACK: Tag line "human experiences, designed", name (i.e. John Doe), job role (i.e. Director, Product Development), phone number, email address, and website. The background color could be a solid color although we are open to suggestions.

Logo Text

ZUM

Font styles to use
Sans Serif

Colors
b768aa
a54499
d2a4cc
876aae
6b449b

Requirements
Must have
• A sense of playfulnesses, charm, excitement, and energy.
• Clean and minimal design
• Avoid using icons for contact information
• NOTE: Not all of the purples that have been chosen must be used. These are only suggestions.

```html
<!DOCTYPE html>
<html lang="en">
<head>
<meta charset="utf-8">
<title>ZUM Business Card</title>
<link href="https://fonts.googleapis.com/css2?family=Source+Sans+3:wght@400;600;700&display=swap" rel="stylesheet">
<style>
  :root {
    --bg-top: #2a2a2a;
    --bg-bottom: #050505;
    --purple: #a54499;
    --purple-text: #9c3b91;
    --white: #ffffff;
    --ink: #4a4a4a;
  }
  * { margin: 0; padding: 0; box-sizing: border-box; }
  html, body { width: 1200px; height: 900px; overflow: hidden; }
  body {
    position: relative;
    background: linear-gradient(180deg, var(--bg-top) 0%, #151515 55%, var(--bg-bottom) 100%);
    font-family: "Source Sans 3", "Myriad Pro", sans-serif;
  }
  .card {
    position: absolute;
    top: 306px;
    width: 439px;
    height: 271px;
    border-radius: 12px;
    box-shadow: 0 2px 6px rgba(0,0,0,0.5);
    overflow: hidden;
  }
  .card-front { left: 149px; background: var(--white); }
  .card-back { left: 609px; background: var(--purple); }

  .wordmark {
    position: absolute;
    font-weight: 700;
    line-height: 1;
    white-space: nowrap;
  }
  .card-front .wordmark {
    left: 42px; top: 93px;
    width: 176px;
    text-align: center;
    font-size: 88px;
    letter-spacing: 1px;
    color: var(--purple);
  }
  .card-back .wordmark {
    left: 0; right: 0; top: 84px;
    text-align: center;
    font-size: 112px;
    letter-spacing: 1px;
    color: var(--white);
  }
  .tagline {
    position: absolute;
    left: 0; right: 0; top: 201px;
    text-align: center;
    color: var(--white);
    font-size: 14.5px;
  }

  .details { position: absolute; left: 251px; top: 60px; color: var(--ink); font-size: 12.5px; line-height: 16px; }
  .name { color: var(--purple-text); font-weight: 700; font-size: 15px; line-height: 18px; }
  .role { margin-bottom: 10px; }
  .address { margin-bottom: 11px; }
  .contact-list { list-style: none; }
  .contact-list li { display: flex; align-items: center; gap: 6px; }
  .contact-list svg { width: 10px; height: 10px; fill: var(--purple); flex: none; }
</style>
</head>
<body>
  <section class="card card-front">
    <div class="wordmark">ZUM</div>
    <div class="details">
      <div class="name">Daniel Reyes</div>
      <div class="role">Managing Director</div>
      <div class="address">12345, Address Goes Here<br>Country Name, 123456.</div>
      <ul class="contact-list">
        <li>
          <svg viewBox="0 0 10 10" aria-hidden="true"><path d="M2 0.5 L3.8 2.6 L2.9 3.8 Q4 6 6.2 7.1 L7.4 6.2 L9.5 8 L8.3 9.5 Q4.5 9.5 2.5 7.5 Q0.5 5.5 0.5 1.7 Z"/></svg>
          044-555 010 789
        </li>
        <li>
          <svg viewBox="0 0 10 10" aria-hidden="true"><path d="M1 2.5 H9 V7.5 H1 Z M1.5 3 L5 5.6 L8.5 3" stroke="#fff" stroke-width="0.8"/></svg>
          info@zumstudio.example
        </li>
        <li>
          <svg viewBox="0 0 10 10" aria-hidden="true"><circle cx="5" cy="5" r="4.5"/><path d="M0.5 5 H9.5 M5 0.5 Q2.5 5 5 9.5 M5 0.5 Q7.5 5 5 9.5" stroke="#fff" stroke-width="0.6" fill="none"/></svg>
          www.zumstudio.example
        </li>
      </ul>
    </div>
  </section>

  <section class="card card-back">
    <div class="wordmark">ZUM</div>
    <div class="tagline">Human experiences, Designed</div>
  </section>
</body>
</html>
```